Design a brand style for my candle

Hi!
We need a label design created to start off our candle company, we look to create a fun, girly, cool and on trend brand. We are wanting a label to go on candles with a quote on it "Shine On Girl". Please use this quote when submitting your design, if you could place it on a candle that would be awesome. We love the pastel colours of pink, how this is incorporated in other colours we look forward to your designs. I have attached photos as a start of a "mood board" . The font and style must be easily changed to suit other quotes and sayings
Thanks so much!
Updates

Looking for something modern, minimalist, cool and on Trend packaging targeting 20's women Added Thursday, January 5, 2017

Target Market(s)

Women 20-35
Style - Fun, Flirty, Clean Lines and Cool

Industry/Entity Type

Retail

Font styles to use
Sans Serif

Requirements
Must have
• pastel pink, the quote "Shine On Girl" on the candle (pic is an example only, please do not use the same font)

```html
<!DOCTYPE html>
<html lang="en">
<head>
<meta charset="utf-8">
<title>Shine On Girl — Candle Label</title>
<link rel="stylesheet" href="https://fonts.googleapis.com/css2?family=Didact+Gothic&display=swap">
<style>
  :root {
    --canvas-bg: #ffffff;
    --label-pink: #efb3d5;
    --label-ink: #ffffff;
    --art-cream: #fdfbf2;
  }
  * { margin: 0; padding: 0; box-sizing: border-box; }
  html, body {
    width: 1200px;
    height: 1200px;
    overflow: hidden;
    background: var(--canvas-bg);
  }
  .canvas {
    position: relative;
    width: 1200px;
    height: 1200px;
    background: var(--canvas-bg);
  }
  .candle-label {
    position: absolute;
    left: 200px;
    top: 220px;
    width: 800px;
    height: 760px;
  }
  .label-shape {
    position: absolute;
    inset: 0;
    width: 100%;
    height: 100%;
  }
  .label-shape path { fill: var(--label-pink); }
  .mascot-art {
    position: absolute;
    left: 262px;
    top: 60px;
    width: 316px;
    height: 350px;
    background: var(--art-cream);
    border-radius: 46% 40% 30% 38% / 38% 44% 30% 40%;
  }
  .quote {
    position: absolute;
    left: 0;
    right: 0;
    top: 462px;
    text-align: center;
    font-family: "Didact Gothic", sans-serif;
    font-weight: 400;
    font-size: 96px;
    line-height: 1;
    letter-spacing: -1px;
    color: var(--label-ink);
    white-space: nowrap;
  }
  .company-name {
    position: absolute;
    left: 0;
    right: 0;
    top: 640px;
    text-align: center;
    font-family: "Didact Gothic", sans-serif;
    font-weight: 400;
    font-size: 46px;
    line-height: 1;
    color: var(--label-ink);
    white-space: nowrap;
  }
</style>
</head>
<body>
  <main class="canvas">
    <section class="candle-label">
      <svg class="label-shape" viewBox="0 0 800 760" aria-hidden="true">
        <path d="M 110 20 L 690 20 C 700 70 730 100 780 110 C 760 200 770 330 800 380 C 770 430 760 560 780 650 C 730 660 700 690 690 740 L 110 740 C 100 690 70 660 20 650 C 40 560 30 430 0 380 C 30 330 40 200 20 110 C 70 100 100 70 110 20 Z"/>
      </svg>
      <div class="mascot-art" role="img" aria-label="Cream silhouette of a unicorn head with flowing curled mane"></div>
      <p class="quote">Shine On Girl</p>
      <p class="company-name">company name</p>
    </section>
  </main>
</body>
</html>
```